New Corporate Email Signature with Custom GIF VAM Electric LLC & VAM Fire & Security

Project Overview
VAM Electric LLC and VAM Fire & Security are seeking a professional, polished, and technically robust corporate email signature design. The project has two integrated deliverables:
A custom animated GIF representing both sides of our business
A complete corporate email signature layout designed for real-world compatibility (Gmail, Outlook, iOS, Android)
Our brand aesthetic is corporate, conservative, and clean. We value clarity, trust, professionalism, and subtle creativity β€” nothing overly flashy or cartoonish.
This design will be used across the entire company and must be visually aligned with our brand while remaining technically dependable.

PART 1 β€” Animated GIF Requirements
The GIF will be the core visual anchor of the new signature.
It must be clean, smooth, subtle, and optimized for email use.
βš™ Technical Requirements
Max file size: 150–200 KB (smaller is better)
Dimensions: approx 300px width (flexible, but must look good small)
Looping: continuous loop
Style: professional, minimalistic transitions

No rapid flashing or harsh animations
Must export cleanly into a format email clients accept

🎞 GIF Animation Sequence
Phase 1 β€” VAM Electric (VE)
Use the yellow β€œVE” avatar logo (provided).
Animation flow:
VE avatar appears
Full name β€œVAM Electric LLC” slides in, fades in, or otherwise appears smoothly
A scrolling or cycling list of service offerings displays:
EV Charging Stations
Generator & Transformers
Testing & Troubleshooting
LED Lighting Upgrades
After the list is shown, the entire VE segment fades out

Phase 2 β€” VAM Fire & Security (VF)
Use the red β€œVF” avatar logo (provided).
Animation flow mirrors Phase 1:
VF avatar appears
Full name β€œVAM Fire & Security” slides/fades in
Scrolling or cycling list of services displays:
Fire Alarm Upgrades
KDLT 58 Test & Inspect
Security Surveillance Systems
Access Control Systems
Data & Fiber Optic Cabling
Fade out β†’ loop back to VE
Creative Direction

Designers are encouraged to use:
Clean transitions
Soft fades
Professional typography
Modern minimalism
Consistent brand colors
High clarity at small sizes

Avoid:
Busy motion
Hard flashes
Excessive text overlays
Overly long transitions

The goal: a smooth, corporate-grade rotation that fits seamlessly into an email signature.

PART 2 β€” Corporate Email Signature Design

The signature must be visually appealing, brand-aligned, and structurally bulletproof across all major email systems.
πŸ“ Required Elements
πŸ‘€ Left Side Content
Circular headshot (we will supply final photos)
Social media icons with embedded URLs:
Facebook
LinkedIn
Google Business Profile
Instagram

Icons should be clean, modern, and in alignment with brand colors
πŸ“„ Right Side Content
Name
Title
VAM Electric LLC / VAM Fire & Security (depending on user)
Phone number
Email address
License# 42860
Physical office address: 348 Brambleton Ave, Ferncliff NJ 07391

Small CTA for newsletter signup (button or micro-banner)

🏒 Branding Assets Provided

You will receive:
VE avatar logo
VF avatar logo
Full-name VE logo
Full-name VF logo

These should be incorporated naturally and professionally.

Design Requirements

Conservative corporate styling

Clean typography

Balanced use of white space

Professional hierarchy

Light and dark mode compatibility preferred

Layout should not rely on one large image

All images should export cleanly for hosting on servers/CDN

Avoid overly tall signatures

The final signature must present as modern, trustworthy, and technically reliable across platforms.

πŸ§ͺ Compatibility Requirements

The signature must display correctly in:

Gmail (web and mobile)

Outlook (desktop & online)

Apple Mail

iPhone Mail

Android mail apps

Designers must avoid DIV-based layouts and instead propose a layout that can be implemented using table-based HTML, which is the industry standard for email compatibility.

You do not need to build the HTML β€” only supply the final layered design (PSD/AI/Figma) plus a clear structural layout that can be converted to HTML later.

πŸ“¦ Deliverables
1. Animated GIF

Final optimized GIF

Source file (After Effects, Photoshop, or equivalent)

Export guidelines so we can reproduce future versions

2. Email Signature Design

Full static design mockup

Modular layout for each employee

Icon set for social media

Newsletter CTA element

Clear spacing, alignment, and typography specifications

All source files (PSD, AI, Figma, etc.)

🧭 Creative Guidance Summary

We want:
βœ” Modern
βœ” Corporate
βœ” Minimalistic
βœ” Professional
βœ” Clean motion
βœ” Consistent branding
βœ” Email-safe elements

We do not want:
✘ Flashy marketing look
✘ Overly colorful or playful styles
✘ Hard-to-read fonts
✘ Heavy animation
✘ Oversized signatures

πŸ›  Tools & Format Flexibility

We allow full creative freedom regarding:

Animation style

Typography choices

Structuring of the two-column layout

How the service lists scroll or cycle

As long as the end result is clean, brand-aligned, professional, and email-compatible.

πŸ’¬ Final Note to Designers

We encourage creativity within the boundaries of corporate professionalism.
This signature will represent our company every time an email is sent β€” it must communicate trust, clarity, expertise, and brand strength.

```html
<!DOCTYPE html>
<html lang="en">
<head>
<meta charset="utf-8">
<title>VAM Electric LLC – Email Signature</title>
<link rel="stylesheet" href="https://fonts.googleapis.com/css2?family=Poppins:wght@400;500;600;700&display=swap">
<style>
  :root {
    --brand-yellow: #f2cf1d;
    --brand-gray: #6e6e6e;
    --band-gray: #8a8a8a;
    --ring-gray: #d9d9d9;
    --photo-tone: #c9c3bb;
    --text-dark: #2a2a2a;
    --text-body: #333333;
    --paper: #ffffff;
  }
  * { box-sizing: border-box; margin: 0; padding: 0; }
  html, body {
    width: 1200px; height: 300px; overflow: hidden;
    background: var(--paper);
  }
  .signature {
    position: relative; width: 1200px; height: 300px; overflow: hidden;
    background: var(--paper);
    font-family: "Poppins", Arial, sans-serif;
    color: var(--text-body);
  }
  .signature__shapes { position: absolute; inset: 0; }

  .headshot {
    position: absolute; left: 40px; top: 20px;
    width: 200px; height: 200px; border-radius: 50%;
    background: var(--ring-gray); padding: 8px;
  }
  .headshot__photo {
    width: 100%; height: 100%; border-radius: 50%;
    background: radial-gradient(circle at 50% 40%, #e2ddd6 0%, var(--photo-tone) 60%, #a89f95 100%);
  }

  .socials {
    position: absolute; left: 70px; top: 242px;
    display: flex; gap: 18px; list-style: none;
  }
  .socials__item {
    width: 28px; height: 28px; border-radius: 50%;
    background: var(--brand-yellow);
    box-shadow: 0 0 0 2px var(--paper);
  }

  .company-name {
    position: absolute; left: 356px; top: 8px;
    font-size: 38px; font-weight: 700; letter-spacing: 2px;
    text-transform: uppercase; color: var(--brand-gray);
    line-height: 1.2;
  }

  .person { position: absolute; left: 364px; top: 76px; }
  .person__name {
    font-size: 30px; font-weight: 600; color: var(--text-dark); line-height: 1.2;
  }
  .person__title {
    font-size: 20px; font-weight: 400; color: var(--text-body);
    margin-top: 8px; padding-bottom: 8px; width: 240px;
    border-bottom: 2px solid var(--ring-gray);
  }

  .newsletter-cta {
    position: absolute; left: 842px; top: 74px;
    width: 318px; height: 62px; border-radius: 31px;
    background: var(--brand-gray); color: var(--paper);
    font-size: 24px; font-weight: 500;
    display: flex; align-items: center; justify-content: center;
    text-decoration: none;
  }

  .contacts { position: absolute; left: 362px; top: 180px; list-style: none; }
  .contacts__row { display: flex; height: 52px; align-items: center; }
  .contact { display: flex; align-items: center; font-size: 21px; color: var(--text-dark); }
  .contact--first { width: 290px; }
  .contact__icon {
    width: 34px; height: 34px; border-radius: 50%;
    background: var(--brand-yellow); margin-right: 20px; flex: none;
    display: flex; align-items: center; justify-content: center;
  }
  .contact__icon svg { width: 18px; height: 18px; fill: var(--brand-gray); }
</style>
</head>
<body>
<main class="signature">
  <svg class="signature__shapes" width="1200" height="300" viewBox="0 0 1200 300" aria-hidden="true">
    <path d="M0 130 Q50 190 150 215 L300 300 L0 300 Z" fill="var(--brand-yellow)"/>
    <path d="M200 150 L238 150 L372 300 L330 300 Z" fill="var(--band-gray)"/>
    <path d="M1010 0 L1200 0 L1200 110 Q1130 60 1010 0 Z" fill="var(--brand-yellow)"/>
    <path d="M1060 0 L1110 0 L1200 48 L1200 78 Z" fill="var(--band-gray)" opacity="0.55"/>
  </svg>

  <div class="headshot">
    <div class="headshot__photo" role="img" aria-label="Circular headshot of the team member"></div>
  </div>

  <ul class="socials" aria-label="Social profiles">
    <li class="socials__item" role="img" aria-label="Social profile link"></li>
    <li class="socials__item" role="img" aria-label="Business profile link"></li>
    <li class="socials__item" role="img" aria-label="Professional network link"></li>
    <li class="socials__item" role="img" aria-label="Photo profile link"></li>
  </ul>

  <h1 class="company-name">VAM Electric LLC</h1>

  <div class="person">
    <p class="person__name">Marco</p>
    <p class="person__title">Project Manager</p>
  </div>

  <a class="newsletter-cta" href="#newsletter">Join Our Newsletter</a>

  <ul class="contacts">
    <li class="contacts__row">
      <span class="contact contact--first">
        <span class="contact__icon"><svg viewBox="0 0 24 24"><path d="M6.6 10.8a15.1 15.1 0 0 0 6.6 6.6l2.2-2.2a1 1 0 0 1 1-.25 11.4 11.4 0 0 0 3.6.57 1 1 0 0 1 1 1V20a1 1 0 0 1-1 1A17 17 0 0 1 3 4a1 1 0 0 1 1-1h3.5a1 1 0 0 1 1 1c0 1.25.2 2.45.57 3.57a1 1 0 0 1-.25 1z"/></svg></span>
        +1 555 014 2286
      </span>
      <span class="contact">
        <span class="contact__icon"><svg viewBox="0 0 24 24"><path d="M3 5h18a1 1 0 0 1 1 1v12a1 1 0 0 1-1 1H3a1 1 0 0 1-1-1V6a1 1 0 0 1 1-1zm9 7 8-5H4z"/></svg></span>
        support@vamelectric.com
      </span>
    </li>
    <li class="contacts__row">
      <span class="contact contact--first">
        <span class="contact__icon"><svg viewBox="0 0 24 24"><path d="M4 4h16a1 1 0 0 1 1 1v14a1 1 0 0 1-1 1H4a1 1 0 0 1-1-1V5a1 1 0 0 1 1-1zm2 4v2h6V8zm0 4v2h8v-2zm9-4v5h3V8z"/></svg></span>
        License# 42860
      </span>
      <span class="contact">
        <span class="contact__icon"><svg viewBox="0 0 24 24"><path d="M12 2a7 7 0 0 1 7 7c0 5-7 13-7 13S5 14 5 9a7 7 0 0 1 7-7zm0 4.5A2.5 2.5 0 1 0 12 11.5 2.5 2.5 0 0 0 12 6.5z"/></svg></span>
        348 Brambleton Ave, Ferncliff NJ 07391
      </span>
    </li>
  </ul>
</main>
</body>
</html>
```